Business Card design for construction company

I would like a business card design for a construction company - Harlow Constructions. I have attached the ai logo file for use. I would like the card to be very smart and clean and incorporate only white and the two colours in the logo. I would like the card to have two sides. One side can just have the logo, the other with the relevant information.

Target Market(s)

Building and Construction Clients

Industry/Entity Type

Business

Contact Information for Business Card

Name: Tom Pardoe
Company: Harlow Constructions Pty Limited
Address: 14 Mallee Crescent Carrow Vale 2093
Phone: 0427 531 068
Email: tomp@harlowbuild-example.com.au

Font styles to use
Serif
Sans Serif

Requirements
Must have
• Details noted above
• Logo as provided
• Colours as in logo
• Square edges
• A font that compliments the logo
Should not have
• Any colour other than white and those in logo
• Rounded edges

```html
<!DOCTYPE html>
<html lang="en">
<head>
<meta charset="utf-8">
<title>Harlow Constructions – Business Card</title>
<link rel="stylesheet" href="https://fonts.googleapis.com/css2?family=Montserrat:wght@500;600;700;800&display=swap">
<style>
  :root {
    --backdrop: #2c2c2e;
    --card-white: #eff7fb;
    --brand-blue: #00adee;
    --brand-grey: #525458;
    --text-white: #ffffff;
  }
  * { margin: 0; padding: 0; box-sizing: border-box; }
  html, body {
    width: 1200px;
    height: 1200px;
    overflow: hidden;
    background: var(--backdrop);
    font-family: "Montserrat", Arial, sans-serif;
  }
  .card {
    position: absolute;
    left: 217px;
    width: 736px;
    height: 421px;
  }
  .card--front {
    top: 106px;
    background: var(--card-white);
    display: flex;
    align-items: center;
    justify-content: center;
  }
  .wordmark {
    display: flex;
    align-items: center;
    gap: 16px;
    margin-top: -14px;
  }
  .wordmark__square {
    width: 14px;
    height: 14px;
    background: var(--brand-blue);
  }
  .wordmark__name {
    font-weight: 500;
    font-size: 34px;
    letter-spacing: 2px;
    color: var(--brand-grey);
    text-transform: uppercase;
  }
  .card--back {
    top: 596px;
    background: var(--brand-blue);
    color: var(--text-white);
  }
  .holder {
    position: absolute;
    top: 56px;
    left: 0;
    width: 100%;
    text-align: center;
    margin-left: -2px;
  }
  .holder__name {
    font-weight: 800;
    font-size: 34px;
    letter-spacing: -1px;
    line-height: 36px;
  }
  .holder__company {
    font-weight: 700;
    font-size: 16px;
    letter-spacing: 2px;
    text-transform: uppercase;
    line-height: 18px;
  }
  .contacts {
    position: absolute;
    right: 60px;
    top: 250px;
    list-style: none;
  }
  .contacts__item {
    display: flex;
    justify-content: flex-end;
    align-items: center;
    gap: 7px;
    font-weight: 700;
    font-size: 14.5px;
    letter-spacing: 2px;
    text-transform: uppercase;
    height: 29px;
  }
  .contacts__item--phone { font-size: 16.5px; }
  .contacts__icon {
    width: 15px;
    height: 15px;
    fill: var(--text-white);
    flex: none;
  }
</style>
</head>
<body>
  <section class="card card--front" aria-label="Card front">
    <div class="wordmark">
      <span class="wordmark__square"></span>
      <span class="wordmark__name">Harlow Constructions</span>
    </div>
  </section>

  <section class="card card--back" aria-label="Card back">
    <div class="holder">
      <h1 class="holder__name">Tom Pardoe</h1>
      <p class="holder__company">Harlow Constructions Pty Limited</p>
    </div>
    <ul class="contacts">
      <li class="contacts__item contacts__item--phone">0427-531-068
        <svg class="contacts__icon" viewBox="0 0 16 16"><path d="M3.5 1l2.5 3-1.5 1.8c.9 2 2.4 3.6 4.4 4.6L10.7 9l3.3 2.4-1 2.8C7.5 14 2 8.5 1.6 2.6z"/></svg>
      </li>
      <li class="contacts__item">tomp@harlowbuild-example.com.au
        <svg class="contacts__icon" viewBox="0 0 16 16"><path d="M1 3h14v1.5L8 9 1 4.5z"/><path d="M1 6l7 4.5L15 6v7H1z"/></svg>
      </li>
      <li class="contacts__item">www.harlowbuild-example.com.au
        <svg class="contacts__icon" viewBox="0 0 16 16"><circle cx="8" cy="8" r="7"/><path d="M5 4l3 1-1 3 2 2-1 3-2-3-2-1z" fill="#00adee"/></svg>
      </li>
      <li class="contacts__item">14 Mallee Crescent Carrow Vale 2093
        <svg class="contacts__icon" viewBox="0 0 16 16"><path d="M8 0.5a5 5 0 0 1 5 5c0 3.5-5 10-5 10s-5-6.5-5-10a5 5 0 0 1 5-5zm0 3a2 2 0 1 0 0 4 2 2 0 0 0 0-4z"/></svg>
      </li>
    </ul>
  </section>
</body>
</html>
```